Re jig a A4 Instructional Flyer

We need an established A4 instructional Flyer (2 pages x A4) - to be rejigged in Harcourt College of Learning Branding to look fresh and new.

Permissions have been received to rejig this Medical Triage Chart. Fresh branding and setting out (fonts) required.

FOOTER NOTES : to be inserted at the bottom of the A4 instruction sheet

Harcourt College produced with permissions from Outback Care Alliance, produced by Outback Care Alliance with Clinic Circle Uptown with permissions from Southern Lakes Carewell Hub. Harcourt acknowledges the NBFPS Standards Criterion 3.2.3 Practice Training and Education in Triage

Target Market(s)

Medical Practices

Industry/Entity Type

Health

Font styles to use
Serif

Colors
0255a3
f78f20

Requirements
Must have
• Professional
• Pops of colour in the chart.
• This chart is to be USED and is VISUAL (no boring grey words throughout)
• PROBS SANS SERIF but SERIF for titles OK
Nice to have
• look at www.harcourtlearn.edu.au FOR BRANDING look and feel

```html
<!DOCTYPE html>
<html lang="en">
<head>
<meta charset="utf-8">
<title>Front Desk Triage – Harcourt College of Learning</title>
<link rel="stylesheet" href="https://fonts.googleapis.com/css2?family=Montserrat:wght@500;600&family=Source+Sans+3:ital,wght@0,400;0,600;0,700;1,400&display=swap">
<style>
  :root{
    --cream:#f9efe5;
    --brand-orange:#d18d50;
    --panel:#3b3b3d;
    --panel-accent:#eba936;
    --ink:#222;
    --rule:#555;
    --alert-red:#e3101b;
    --cat1:#e31b23;
    --cat2:#ee7d1d;
    --cat3:#f8c22b;
    --cat4:#1a9a8f;
    --cat5:#5c2d82;
    --cat6:#7fae2e;
    --note-bar:#d9914f;
  }
  *{box-sizing:border-box;margin:0;padding:0}
  html,body{width:1200px;height:848px;overflow:hidden;background:#fff}
  body{position:relative;font-family:"Source Sans 3",Arial,sans-serif;color:var(--ink);font-size:13px;line-height:17.2px}

  .header-band{position:absolute;left:0;top:0;width:1200px;height:128px;background:var(--cream)}
  .title-block{position:absolute;left:26px;top:0;width:415px;height:128px;background:var(--brand-orange)}
  .brand-box{position:absolute;left:13px;top:12px;width:110px;height:102px;background:#fff;display:flex;align-items:center;justify-content:center;text-align:center;padding:8px}
  .brand-name{font-family:"Source Sans 3",Arial,sans-serif;font-weight:700;font-size:12px;line-height:15px;color:#2a3550;text-transform:uppercase;letter-spacing:.5px}
  .title{position:absolute;left:148px;top:30px;font-family:"Montserrat",Arial,sans-serif;font-weight:500;font-size:37px;line-height:35px;color:#fff;letter-spacing:.5px}
  .subtitle{position:absolute;left:466px;top:44px;font-family:"Montserrat",Arial,sans-serif;font-weight:500;font-size:18px;line-height:21px;color:#222}

  .action-panel{position:absolute;left:916px;top:0;width:255px;height:319px;background:var(--panel);color:#fff;padding:38px 22px 0 22px}
  .action-title{display:flex;align-items:center;gap:9px;font-family:"Montserrat",Arial,sans-serif;font-weight:600;font-size:15px;color:var(--panel-accent);margin-left:-2px;margin-bottom:10px}
  .action-list{list-style:none}
  .action-list li{font-size:13.5px;line-height:20px;padding:6px 0 6px 0;border-bottom:1px solid #8a8a8a;margin-left:2px;margin-right:6px}
  .action-call{font-style:italic;font-weight:600;color:var(--panel-accent);font-size:14px;line-height:20px;padding-top:8px;margin-left:2px}

  .col{position:absolute;top:166px}
  .col h2{font-size:13.6px;font-weight:700;line-height:18px;padding-bottom:7px;border-bottom:1px solid var(--rule);margin-bottom:11px}
  .col-1{left:36px;width:261px}
  .col-2{left:330px;width:257px;top:164px}
  .col-3{left:622px;width:257px;top:165px}
  .col-4{left:916px;width:244px;top:355px}

  .bullets{list-style:none}
  .bullets li{position:relative;padding-left:12px;margin-bottom:11px}
  .bullets li::before{content:"•";position:absolute;left:0;top:0;font-size:11px}
  .col-3 .bullets li{margin-bottom:11.5px}

  .steps{list-style:none}
  .steps li{margin-bottom:8.5px;padding-left:12px;text-indent:-12px}

  .cats{list-style:none}
  .cat{position:relative;padding-left:28px;margin-bottom:13px}
  .cat-dot{position:absolute;left:0;top:1px;width:18px;height:18px;border-radius:50%;color:#fff;font-size:9.5px;font-weight:700;display:flex;align-items:center;justify-content:center}
  .cat em{font-style:italic}
  .alert{color:var(--alert-red);font-weight:700}

  .record-note{position:absolute;left:918px;top:680px;width:230px;height:123px;border-left:3px solid var(--note-bar);padding:5px 0 0 20px;font-style:italic;font-size:11.8px;line-height:18.4px}

  .footer{position:absolute;left:43px;top:814px;font-size:7.5px;line-height:10px;color:#222}
</style>
</head>
<body>

<div class="header-band"></div>
<div class="title-block">
  <div class="brand-box"><span class="brand-name">Harcourt College of Learning</span></div>
  <h1 class="title">FRONT DESK<br>TRIAGE</h1>
</div>
<p class="subtitle">How to manage common scenarios<br>faced by reception staff</p>

<aside class="action-panel">
  <div class="action-title">
    <svg width="20" height="20" viewBox="0 0 20 20" aria-hidden="true"><circle cx="10" cy="10" r="10" fill="#f3c22a"/><rect x="8.8" y="4" width="2.4" height="8" rx="1" fill="#3b3b3d"/><circle cx="10" cy="15" r="1.4" fill="#3b3b3d"/></svg>
    Emergency Action Plan
  </div>
  <ul class="action-list">
    <li>Remain calm and do not panic</li>
    <li>Be aware and respond to<br>the needs of the emergency</li>
    <li>Assess which patient needs<br>to take priority</li>
    <li>Deal with any injury or<br>illness in order of severity</li>
  </ul>
  <p class="action-call">CALL 000 FOR<br>AMBULANCE, POLICE OR FIRE</p>
</aside>

<section class="col col-1">
  <h2>Is this an emergency?</h2>
  <ul class="bullets">
    <li>When answering the telephone, all callers should be asked if the matter is an emergency prior to being placed on hold: Ask the patient, “Is this an emergency or can I place you on hold for a moment?”</li>
    <li>Consider the <b><i>Triage Steps</i></b> and <b><i>Categories</i></b> listed on the reverse of this document to assess the patient’s status.</li>
  </ul>
  <h2 style="margin-top:28px">Ask the patient – Triage Steps</h2>
  <ol class="steps">
    <li>1. Confirm the patient’s name and phone number.</li>
    <li>2. Does the patient attend the surgery? (ie Does the practice have previous medical records to hand?)</li>
    <li>3. Location. (“Are you at home?” “Are you alone?”)</li>
    <li>4. Nature of their problem. (Patient may prefer to speak to the practice nurse or on call doctor.)</li>
    <li>5. Duration of their symptoms. (“How long have you felt like this?”)</li>
    <li>6. Severity of their problem. (“On a scale of 1 to 10 how severe is the pain?” [if applicable].)</li>
    <li>7. Any previous major health problems. (“Are you on any medication?” “Do you have any allergies?”)</li>
  </ol>
</section>

<section class="col col-2">
  <h2>On the day emergencies in the clinic</h2>
  <ol class="cats">
    <li class="cat"><span class="cat-dot" style="background:var(--cat1)">1</span><em>Category 1 patients:</em> <b>See on-call doctor or other medical professional on duty immediately.</b></li>
    <li class="cat"><span class="cat-dot" style="background:var(--cat2)">2</span><em>Category 2 patients:</em> <b>Direct to the emergency department of their nearest hospital.</b></li>
    <li class="cat"><span class="cat-dot" style="background:var(--cat3)">3</span><em>Category 3 patients or patients with worsening symptoms:</em> Refer to the practice nurse or on call doctor.</li>
    <li class="cat"><span class="cat-dot" style="background:var(--cat4)">4</span><em>Category 4 patients:</em> Advise to attend the clinic immediately and triaged by the practice nurse (may then be slotted in between appointments or at the end of the session).</li>
    <li class="cat"><span class="cat-dot" style="background:var(--cat5)">5</span><em>Category 5 patients:</em> Make an appointment for the day and be advised to call back if symptoms worsen.</li>
    <li class="cat"><span class="cat-dot" style="background:var(--cat6)">6</span><em>Category 6 patients:</em> Make an appointment within 24 hours and call back if symptoms worsen.</li>
  </ol>
</section>

<section class="col col-3">
  <h2>Scheduling care</h2>
  <ul class="bullets">
    <li>Reception staff should reserve several unbooked appointment times each day for ‘on the day’ urgent appointments such as unwell children and the elderly, lacerations and suspected fractures.</li>
    <li>If your practice does not operate on an appointment system, patients should be triaged on walk in and advised of the expected waiting time to see the doctor, nurse or Aboriginal health worker.</li>
    <li>Where a patient is assessed as in need of urgent medical attention over the telephone, advise the caller to hang up and <span class="alert">call 000</span> immediately for an ambulance.</li>
    <li>Where a receptionist is unable to determine the urgency of a telephone call, the patient should be transferred to the practice nurse or on-call doctor for triage.</li>
    <li>If a patient presents in person and requires urgent medical assistance after the doctor has left – <span class="alert">call 000</span> for ambulance.</li>
    <li>Clinical staff treating the patient should wear as a minimum, a surgical mask, gloves and when collecting nose and/or throat swabs, protective eyewear.</li>
  </ul>
</section>

<section class="col col-4">
  <h2>Patients presenting symptoms of potential communicable diseases</h2>
  <ul class="bullets">
    <li>Such as ‘influenza(‘flu), measles, chicken pox should be isolated to a secluded area of the medical practice such as the nurses’ office. Where possible, a notice of isolation is to be fixed to the door to limit access in this area.</li>
    <li>Patients with ‘flu like symptoms should be required to wear a surgical mask.</li>
    <li>If the patient is bleeding or vomiting, put gloves on before you assist them.</li>
  </ul>
</section>

<p class="record-note">All emergency cases dealt with by reception should be recorded by the staff member involved in the patient health record in addition to the clinical notes recorded by the practice nurse or doctor/s treating the patient.</p>

<p class="footer">This resource was developed by Clinic Circle Uptown (2010) and recreated with permission from Southern Lakes Carewell Hub (2014)</p>

</body>
</html>
```